"Your Golden Years Start Tomorrow!" book cover for 80 page or so book.

Need a book cover that stands out on Bookvale, so highly engaging colors, need to reflect optimism, hope and determination. Go to Bookvale, type my name in and see the covers for the three other books I had written.

There's a lot of negativity and fear for Americans looking at retirement. Yet, they don't need that fear, my book tells them why they can be confident in their ability to retire.

There will be NO spine writing for the book, too small.

Target Market(s)

stressed out people in their 50s and 60s. This book appeals to working people, not high end, wealthy types.

Industry/Entity Type

Financial Planning

Colors

Designer to choose colors to be used in the design.

Requirements
Must have
• Needs to reflect simplicity in action.
• Please spell out my full name, MARK DELVORTH, at the bottom of the cover.
Nice to have
• if there is anyway to put a picture of an RV (Recreational Vehicle) that would be great.
Should not have
• Do NOT want to be the stodgy, typical financial planning literature out there. No guy in a suit and tie. No one sitting on a beach.
• Do not want my face on the cover either. (On the back yes.)

```html
<!DOCTYPE html>
<html lang="en">
<head>
<meta charset="utf-8">
<title>Your Golden Years Start Tomorrow! — Book Cover</title>
<link rel="stylesheet" href="https://fonts.googleapis.com/css2?family=Cinzel:wght@500;600;700&display=swap">
<style>
  :root {
    --backdrop: #ece3d2;
    --paper: #ffffff;
    --gold: #e8b622;
    --ink: #111111;
    --rock-light: #c0633a;
    --rock-mid: #9c4527;
    --rock-dark: #6e3020;
    --road: #4d4a48;
  }
  html, body {
    margin: 0;
    padding: 0;
    width: 1200px;
    height: 1118px;
    overflow: hidden;
    background: var(--backdrop);
  }
  .canvas {
    position: relative;
    width: 1200px;
    height: 1118px;
  }
  .book-cover {
    position: absolute;
    left: 232px;
    top: 39px;
    width: 736px;
    height: 1040px;
    display: block;
    background: var(--paper);
    box-shadow: 0 14px 30px rgba(0, 0, 0, 0.18);
  }
  .title-small {
    font-family: 'Cinzel', serif;
    font-weight: 700;
    fill: var(--ink);
  }
  .title-large {
    font-family: 'Cinzel', serif;
    font-weight: 600;
    fill: var(--gold);
  }
  .title-rule {
    stroke: var(--ink);
    stroke-width: 2;
  }
  .author-band { fill: var(--gold); }
  .author-name {
    font-family: 'Cinzel', serif;
    font-weight: 600;
    fill: var(--ink);
  }
</style>
</head>
<body>
<main class="canvas">
  <svg class="book-cover" viewBox="0 0 736 1040" xmlns="http://www.w3.org/2000/svg">
    <defs>
      <linearGradient id="landscape-tones" x1="0" y1="0" x2="0" y2="1">
        <stop offset="0" stop-color="var(--rock-light)"/>
        <stop offset="0.35" stop-color="var(--rock-mid)"/>
        <stop offset="0.62" stop-color="var(--rock-dark)"/>
        <stop offset="0.72" stop-color="#7d7a4a"/>
        <stop offset="0.80" stop-color="var(--road)"/>
        <stop offset="1" stop-color="#3e3c3b"/>
      </linearGradient>
    </defs>

    <rect class="cover-paper" x="0" y="0" width="736" height="1040" fill="var(--paper)"/>

    <!-- Title block -->
    <line class="title-rule" x1="57" y1="68" x2="275" y2="68"/>
    <text class="title-small" x="293" y="86" font-size="52" textLength="150" lengthAdjust="spacingAndGlyphs">YOUR</text>
    <line class="title-rule" x1="461" y1="68" x2="680" y2="68"/>

    <text class="title-large" x="62" y="232" font-size="176" textLength="614" lengthAdjust="spacingAndGlyphs">GOLDEN</text>

    <line class="title-rule" x1="57" y1="273" x2="262" y2="273"/>
    <text class="title-small" x="278" y="291" font-size="52" textLength="180" lengthAdjust="spacingAndGlyphs">YEARS</text>
    <line class="title-rule" x1="474" y1="273" x2="680" y2="273"/>

    <text class="title-large" x="60" y="432" font-size="168" textLength="616" lengthAdjust="spacingAndGlyphs">START</text>
    <text class="title-large" x="62" y="546" font-size="122" textLength="614" lengthAdjust="spacingAndGlyphs">TOMORROW!</text>

    <!-- Landscape photograph area -->
    <rect class="cover-photo" x="0" y="572" width="736" height="366" fill="url(#landscape-tones)" role="img" aria-label="Photo of a desert highway leading toward red rock mountains under an open sky"/>

    <!-- Author band -->
    <rect class="author-band" x="0" y="938" width="736" height="102"/>
    <text class="author-name" x="94" y="1006" font-size="46" textLength="548" lengthAdjust="spacing">MARK DELVORTH</text>
  </svg>
</main>
</body>
</html>
```